Business card design needed

We need a business card for a consulting company called Harbor Business Consulting which covers a range of business services in construction and Human Resources. We have chosen balck and red as the colours and have an idea for the logo of a person with arms outstretched signifying all encompassing. See attachment.
Industry/Entity Type
Construction
Contact Information for Business Card
Dennis Holloway
Business Advisor/Site Coordinator/ Licensed Builder (Cert IV Bldg & Site Mgmt)
Mobile: 0481 362 954
Email: dennisholloway@harborconsulting.com.au
PO Box 7814
Kelvin Heights, VIC, 3056, Australia
Logo Text
Harbor Business Consulting
Look and feel

```html
<!DOCTYPE html>
<html lang="en">
<head>
<meta charset="utf-8">
<title>Harbor Business Consulting – Business Cards</title>
<link rel="stylesheet" href="https://fonts.googleapis.com/css2?family=Josefin+Sans:wght@400;600&family=Arimo:wght@700&display=swap">
<style>
  :root {
    --red: #e3191c;
    --red-deep: #c81014;
    --red-faint: #d3141a;
    --red-mark: #b80d12;
    --black: #0c0c0c;
    --tan: #d9a17e;
    --white: #ffffff;
    --page: #ece8e2;
  }
  * { box-sizing: border-box; margin: 0; padding: 0; }
  html, body { width: 1200px; height: 1000px; overflow: hidden; }
  body { background: var(--page); position: relative; font-family: "Josefin Sans", sans-serif; }

  .card {
    position: absolute;
    width: 560px; height: 332px;
    overflow: hidden;
    background: radial-gradient(ellipse at 70% 35%, var(--red) 0%, var(--red-deep) 100%);
    box-shadow: 0 4px 14px rgba(0,0,0,.25);
  }
  .card--front { left: 30px; top: 58px; }
  .card--alt   { left: 580px; top: 288px; }

  .card__shapes { position: absolute; inset: 0; width: 100%; height: 100%; }

  .company {
    position: absolute; right: 22px; top: 40px; width: 300px;
    text-align: center; color: var(--white);
  }
  .company__name {
    font-family: "Arimo", sans-serif; font-weight: 700;
    font-size: 20px; line-height: 23px; letter-spacing: .3px;
  }
  .company__name .company__line2 { font-size: 18px; }
  .card--alt .company__name { font-size: 23px; line-height: 27px; }
  .card--alt .company__name .company__line2 { font-size: 20px; }
  .company__tagline { font-size: 10px; letter-spacing: 1.4px; margin-top: 4px; font-weight: 400; }
  .card--alt .company__tagline { font-size: 13px; margin-top: 0; }

  .contact { position: absolute; left: 20px; top: 152px; width: 240px; color: var(--white); }
  .contact__name { font-size: 15px; font-weight: 400; letter-spacing: 1.3px; margin-bottom: 14px; }
  .contact__role { font-size: 9.5px; line-height: 14px; font-weight: 400; }
  .contact__role small { font-size: 6px; }
  .contact__lines { font-size: 9.5px; line-height: 14px; margin-top: 20px; font-weight: 400; }
  .contact__lines b { font-weight: 600; }
  .contact__address { font-size: 9.5px; line-height: 14px; margin-top: 12px; font-weight: 400; }

  .brand-mark {
    position: absolute; display: flex; align-items: center; justify-content: center;
    border-radius: 50%; text-align: center;
  }
  .card--front .brand-mark {
    left: 415px; top: 204px; width: 108px; height: 108px;
    border: 1.5px solid var(--black);
  }
  .card--front .brand-mark__name { color: var(--black); font-size: 12px; font-weight: 600; line-height: 14px; }
  .card--alt .brand-mark {
    left: 385px; top: 178px; width: 186px; height: 186px;
    background: var(--red-faint);
  }
  .card--alt .brand-mark__name { color: var(--red-mark); font-size: 15px; font-weight: 600; line-height: 18px; }
</style>
</head>
<body>

<section class="card card--front">
  <svg class="card__shapes" viewBox="0 0 560 332" aria-hidden="true">
    <path d="M150,40 L274,256 Q284,280 264,302 L236,332 H226 L256,300 Q273,281 263,262 Z" fill="var(--tan)"/>
    <path d="M0,0 H112 L263,262 Q273,282 256,300 L226,332 H0 Z" fill="var(--black)"/>
  </svg>
  <header class="company">
    <h1 class="company__name">HARBOR BUSINESS<br><span class="company__line2">CONSULTING Pty Ltd</span></h1>
    <p class="company__tagline">BUILDING YOUR GOALS</p>
  </header>
  <div class="contact">
    <h2 class="contact__name">DENNIS HOLLOWAY</h2>
    <p class="contact__role">Business Advisor/Site Coordinator/<br>Licensed Builder <small>(Cert IV Bldg &amp; Site Mgmt)</small></p>
    <p class="contact__lines"><b>Mobile:</b> 0481 362 954<br><b>Email:</b> dennisholloway@harborconsulting.com.au</p>
    <p class="contact__address">PO Box 7814<br>Kelvin Heights, VIC,<br>3056, Australia</p>
  </div>
  <div class="brand-mark"><span class="brand-mark__name">Harbor Business<br>Consulting</span></div>
</section>

<section class="card card--alt">
  <svg class="card__shapes" viewBox="0 0 560 332" aria-hidden="true">
    <path d="M150,40 L274,256 Q284,280 264,302 L236,332 H226 L256,300 Q273,281 263,262 Z" fill="var(--tan)"/>
    <path d="M0,0 H112 L263,262 Q273,282 256,300 L226,332 H0 Z" fill="var(--black)"/>
  </svg>
  <div class="brand-mark"><span class="brand-mark__name">Harbor Business<br>Consulting</span></div>
  <header class="company">
    <h1 class="company__name">HARBOR BUSINESS<br><span class="company__line2">CONSULTING Pty Ltd</span></h1>
    <p class="company__tagline">BUILDING YOUR GOALS</p>
  </header>
  <div class="contact">
    <h2 class="contact__name">DENNIS HOLLOWAY</h2>
    <p class="contact__role">Business Advisor/Site Coordinator/<br>Licensed Builder <small>(Cert IV Bldg &amp; Site Mgmt)</small></p>
    <p class="contact__lines"><b>Mobile:</b> 0481 362 954<br><b>Email:</b> dennisholloway@harborconsulting.com.au</p>
    <p class="contact__address">PO Box 7814<br>Kelvin Heights, VIC,<br>3056, Australia</p>
  </div>
</section>

</body>
</html>
```